Help me make landing pages for my web application that are mobile friendly

I need to make 2 mobile friendly landing pages for an application. The 2 pages will be related. First I need a home page and then I need a working page. I do not want to change the color scheme or logos. Just layout and design.

```html
<!DOCTYPE html>
<html lang="en">
<head>
<meta charset="utf-8">
<title>ShiftCover – Mobile Screens</title>
<link rel="stylesheet" href="https://fonts.googleapis.com/css2?family=Lato:wght@400;700&display=swap">
<style>
:root{
  --page:#f1eff1;
  --white:#ffffff;
  --ink:#2f2f35;
  --ink-soft:#4a4a52;
  --purple:#6a4fa3;
  --label:#5b4aa8;
  --teal:#2aa9d5;
  --green:#2bb24a;
  --red:#e2232c;
  --card-top:#d9e9f3;
  --card-bottom:#e4dff0;
  --line:#e4e4ea;
  --icon-bg:#eef0f6;
}
*{box-sizing:border-box;margin:0;padding:0}
html,body{width:906px;height:1200px;overflow:hidden;background:var(--page)}
body{font-family:"Lato",sans-serif;color:var(--ink)}
.stage{position:absolute;left:0;top:0;width:1671px;height:2212px;transform:scale(0.5422);transform-origin:0 0}
.screen{position:absolute;background:var(--white);overflow:hidden;box-shadow:0 2px 10px rgba(0,0,0,.08)}
.screen.rounded{border-radius:34px}

/* status bar */
.status{position:absolute;left:0;right:0;top:16px;height:20px;padding:0 20px;display:flex;justify-content:space-between;align-items:center;font-size:14px;color:var(--ink)}
.status svg{width:66px;height:12px}

/* brand */
.brand{position:absolute;top:48px;left:0;right:0;height:48px;display:flex;align-items:center}
.kebab{width:6px;margin-left:18px;display:flex;flex-direction:column;gap:4px}
.kebab i{display:block;width:4px;height:4px;border-radius:50%;background:var(--purple)}
.brand-name{display:flex;align-items:center;gap:10px;margin-left:44px;font-size:36px;font-weight:400;color:var(--purple);letter-spacing:-.3px}
.brand-dot{width:26px;height:26px;border-radius:50%;background:var(--teal)}

/* info list */
.section-title{font-size:19px;font-weight:400;color:var(--ink)}
.info-list{list-style:none}
.info-item{display:flex;align-items:flex-start;gap:14px}
.info-icon{flex:none;width:40px;height:40px;border-radius:50%;background:var(--icon-bg);box-shadow:0 1px 3px rgba(0,0,0,.12);display:flex;align-items:center;justify-content:center}
.info-icon svg{width:22px;height:22px}
.info-label{font-size:16px;color:var(--label);line-height:1.2}
.info-value{font-size:15px;color:var(--ink-soft);line-height:1.2}
.info-value .ini{color:var(--teal)}

/* soft panels */
.panel{background:linear-gradient(180deg,var(--card-top),var(--card-bottom));border-radius:8px}
.panel-title{font-size:14px;font-weight:700;color:var(--ink)}
.field{background:var(--white);border-radius:6px;display:flex;align-items:center;font-size:13px;color:var(--ink-soft)}
.pill{display:inline-flex;align-items:center;gap:4px;border-radius:10px;color:#fff;font-size:10px;padding:2px 10px}
.pill.teal{background:var(--teal)}
.pill.purple{background:var(--purple)}
.empty-note{background:var(--white);border-radius:6px;text-align:center;color:var(--purple);font-size:13px;font-weight:700}

/* tabs */
.tabs{position:absolute;left:12px;top:126px;display:flex;align-items:center;gap:18px;white-space:nowrap}
.tab{display:flex;align-items:center;gap:6px;font-size:12px;color:var(--ink-soft)}
.tab.active{background:var(--teal);color:#fff;border-radius:18px;padding:8px 14px;box-shadow:0 1px 3px rgba(0,0,0,.2)}
.tab svg{width:16px;height:16px}

/* assignments */
.assign-wrap{position:absolute;left:8px;right:8px;background:var(--white);border-radius:8px;box-shadow:0 0 8px rgba(0,0,0,.08);overflow:hidden}
.assign-head{display:flex;justify-content:space-between;align-items:center}
.assign-head h2{font-weight:400;color:var(--ink)}
.help{border-radius:50%;background:var(--teal);color:#fff;font-weight:700;display:flex;align-items:center;justify-content:center}
.assign-card{display:flex;justify-content:space-between;background:linear-gradient(180deg,var(--card-top),var(--card-bottom));border-radius:6px}
.ac-label{font-weight:700;color:var(--ink)}
.ac-person{display:flex;align-items:center;gap:10px}
.avatar{flex:none;border-radius:50%;display:flex;align-items:center;justify-content:center;color:var(--teal);background:var(--white)}
.avatar.photo{background:linear-gradient(135deg,#c9a68c,#6e564a)}
.ac-name{color:var(--teal)}
.ac-role{color:var(--ink-soft)}
.ac-meta{color:var(--label);line-height:1.2}
.ac-meta .v{color:var(--ink-soft)}
.ac-meta .t{color:var(--ink-soft);display:block}
.badge{display:inline-block;border-radius:10px;color:#fff;text-align:center}
.badge.complete{background:var(--teal)}
.badge.active{background:var(--green)}
.badge.canceled{background:var(--red)}
.edit svg{display:block}

/* large assignment list */
.list-lg .assign-head{padding:24px 14px 16px 17px}
.list-lg .assign-head h2{font-size:21px}
.list-lg .help{width:20px;height:20px;font-size:12px}
.list-lg .assign-card{margin:0 18px 15px 18px;height:135px;padding:14px 16px}
.list-lg .ac-label{font-size:15px;margin-bottom:12px}
.list-lg .avatar{width:36px;height:36px;font-size:19px}
.list-lg .ac-name{font-size:15px}
.list-lg .ac-role{font-size:13px}
.list-lg .ac-right{width:128px}
.list-lg .ac-meta{font-size:11px;margin-top:6px}
.list-lg .badge{font-size:11px;padding:1px 12px;min-width:72px}
.list-lg .edit svg{width:14px;height:14px}

/* small assignment list */
.list-sm .assign-head{padding:18px 14px 16px 16px}
.list-sm .assign-head h2{font-size:19px}
.list-sm .help{width:18px;height:18px;font-size:11px}
.list-sm .assign-card{margin:0 12px 13px 12px;height:122px;padding:12px 14px}
.list-sm .ac-label{font-size:13px;margin-bottom:10px}
.list-sm .avatar{width:33px;height:33px;font-size:17px}
.list-sm .ac-name{font-size:13px}
.list-sm .ac-role{font-size:12px}
.list-sm .ac-right{width:114px}
.list-sm .ac-meta{font-size:10px;margin-top:6px}
.list-sm .badge{font-size:10px;padding:1px 10px;min-width:66px}
.list-sm .edit svg{width:12px;height:12px}

.home-bar{position:absolute;left:50%;bottom:16px;width:142px;height:4px;margin-left:-71px;border-radius:2px;background:linear-gradient(90deg,var(--teal),var(--purple))}

/* menu screen */
.menu{background:linear-gradient(180deg,#56bbdd 0%,#6c8fcc 45%,#6c55aa 100%)}
.menu .brand-name{color:#fff;margin:0}
.menu .brand-dot{background:#fff}
.nav{list-style:none;position:absolute;left:36px;right:36px;top:138px}
.nav li{display:flex;align-items:center;gap:18px;height:64px;margin-bottom:15px;padding-left:26px;font-size:22px;color:#fff}
.nav li.current{background:var(--purple);border-radius:32px}
.nav svg{width:28px;height:28px}
.profile{position:absolute;left:0;right:0;top:468px;text-align:center;color:#fff}
.profile-img{width:98px;height:98px;border-radius:50%;margin:0 auto;background:radial-gradient(circle at 50% 40%,#d6d6d6,#9c9c9c);border:3px solid #fff}
.btn-outline{display:flex;align-items:center;justify-content:center;gap:8px;width:244px;height:48px;margin:0 auto;border:2px solid #fff;border-radius:24px;font-size:21px}
.btn-logout{position:absolute;left:80px;top:794px;width:244px;height:50px;border-radius:25px;background:var(--teal);color:#fff;font-size:21px;display:flex;align-items:center;justify-content:center;gap:8px}
</style>
</head>
<body>
<svg width="0" height="0" style="position:absolute">
  <defs>
    <symbol id="i-doc" viewBox="0 0 24 24"><rect x="4" y="3" width="14" height="18" rx="2" fill="#3a7fc4"/><path d="M7 8h8M7 12h8M7 16h5" stroke="#fff" stroke-width="1.6"/></symbol>
    <symbol id="i-pin" viewBox="0 0 24 24"><path d="M12 2a7 7 0 0 0-7 7c0 5 7 13 7 13s7-8 7-13a7 7 0 0 0-7-7z" fill="#3a7fc4"/><circle cx="12" cy="9" r="2.6" fill="#fff"/></symbol>
    <symbol id="i-search" viewBox="0 0 24 24"><circle cx="14" cy="10" r="6" fill="none" stroke="#3a7fc4" stroke-width="2.4"/><path d="M9.5 14.5L3 21" stroke="#3a7fc4" stroke-width="3" stroke-linecap="round"/></symbol>
    <symbol id="i-people" viewBox="0 0 24 24"><circle cx="7" cy="8" r="3" fill="#6a4fa3"/><circle cx="17" cy="8" r="3" fill="#6a4fa3"/><circle cx="12" cy="11" r="3" fill="#3a7fc4"/><path d="M2 18c0-3 2-5 5-5s5 2 5 5zM12 18c0-3 2-5 5-5s5 2 5 5z" fill="#6a4fa3"/><path d="M7 21c0-3 2-5 5-5s5 2 5 5z" fill="#3a7fc4"/></symbol>
    <symbol id="i-grid" viewBox="0 0 24 24"><rect x="3" y="3" width="8" height="8" rx="2" fill="#3a7fc4"/><circle cx="17" cy="7" r="4" fill="#6a4fa3"/><rect x="3" y="13" width="8" height="8" rx="2" fill="#3a7fc4"/><rect x="13" y="13" width="8" height="8" rx="2" fill="#3a7fc4"/></symbol>
    <symbol id="i-tree" viewBox="0 0 24 24"><rect x="9" y="2" width="6" height="5" fill="#3a7fc4"/><rect x="2" y="16" width="6" height="5" fill="#3a7fc4"/><rect x="16" y="16" width="6" height="5" fill="#3a7fc4"/><path d="M12 7v5M5 16v-4h14v4" stroke="#6a4fa3" stroke-width="2" fill="none"/></symbol>
    <symbol id="i-info" viewBox="0 0 24 24"><path d="M12 2a9 9 0 1 1-6 15.7L3 21l1.3-4.4A9 9 0 0 1 12 2z" fill="#3a7fc4"/><path d="M12 10v6" stroke="#fff" stroke-width="2.4"/><circle cx="12" cy="7" r="1.4" fill="#fff"/></symbol>
    <symbol id="i-clip" viewBox="0 0 24 24"><rect x="5" y="4" width="14" height="18" rx="2" fill="currentColor"/><rect x="9" y="2" width="6" height="4" rx="1" fill="currentColor" stroke="#fff"/><path d="M8 11h8M8 15h8" stroke="#2aa9d5" stroke-width="1.6"/></symbol>
    <symbol id="i-clock" viewBox="0 0 24 24"><circle cx="12" cy="12" r="9" fill="none" stroke="currentColor" stroke-width="2"/><path d="M12 7v5l3 2" stroke="currentColor" stroke-width="2" fill="none"/></symbol>
    <symbol id="i-cal" viewBox="0 0 24 24"><rect x="3" y="5" width="18" height="16" rx="2" fill="#3a7fc4"/><rect x="3" y="5" width="18" height="4" fill="#6a4fa3"/><g fill="#fff"><rect x="6" y="11" width="3" height="3"/><rect x="10.5" y="11" width="3" height="3"/><rect x="15" y="11" width="3" height="3"/><rect x="6" y="15.5" width="3" height="3"/><rect x="10.5" y="15.5" width="3" height="3"/><rect x="15" y="15.5" width="3" height="3"/></g></symbol>
    <symbol id="i-edit" viewBox="0 0 24 24"><path d="M4 17l10-10 3 3-10 10H4z" fill="#3a7fc4"/><path d="M3 22h18" stroke="#3a7fc4" stroke-width="2"/></symbol>
    <symbol id="i-house" viewBox="0 0 24 24"><path d="M2 12L12 3l10 9h-3v9h-5v-6h-4v6H5v-9z" fill="#fff"/></symbol>
    <symbol id="i-hand" viewBox="0 0 24 24"><circle cx="13" cy="5" r="3" fill="#fff"/><path d="M9 10h8v6H9z" fill="#fff"/><path d="M2 19c4 0 6-3 10-3h6v3H8" stroke="#fff" stroke-width="2" fill="none"/></symbol>
    <symbol id="i-exit" viewBox="0 0 24 24"><path d="M5 3h9v18H5z" fill="#fff"/><path d="M14 12h8M19 9l3 3-3 3" stroke="#fff" stroke-width="2" fill="none"/></symbol>
    <symbol id="i-tap" viewBox="0 0 24 24"><path d="M9 3v11l-2-2-2 2 6 8h8l2-8-8-3V3z" fill="#fff"/></symbol>
    <symbol id="i-status" viewBox="0 0 66 12"><rect x="0" y="8" width="3" height="4" fill="#2f2f35"/><rect x="4" y="6" width="3" height="6" fill="#2f2f35"/><rect x="8" y="3" width="3" height="9" fill="#2f2f35"/><rect x="12" y="0" width="3" height="12" fill="#2f2f35"/><path d="M22 4a9 9 0 0 1 12 0M25 7a5 5 0 0 1 6 0" stroke="#2f2f35" stroke-width="1.6" fill="none"/><circle cx="28" cy="10" r="1.4" fill="#2f2f35"/><rect x="42" y="2" width="20" height="9" rx="2" fill="#2f2f35"/><rect x="63" y="5" width="2" height="3" fill="#2f2f35"/></symbol>
  </defs>
</svg>

<main class="stage">

  <!-- Opening information (compact) -->
  <section class="screen rounded" style="left:148px;top:100px;width:357px;height:775px">
    <div class="status"><span>9:45</span><svg><use href="#i-status"/></svg></div>
    <div class="brand"><div class="kebab"><i></i><i></i><i></i></div><div class="brand-name"><span class="brand-dot"></span>ShiftCover</div></div>
    <h1 class="section-title" style="position:absolute;left:27px;top:122px">Opening Information</h1>
    <ul class="info-list" style="position:absolute;left:22px;top:172px">
      <li class="info-item" style="height:60px"><span class="info-icon"><svg><use href="#i-doc"/></svg></span><div><div class="info-label">Summary</div><div class="info-value">Testing-test</div></div></li>
      <li class="info-item" style="height:61px"><span class="info-icon"><svg><use href="#i-pin"/></svg></span><div><div class="info-label">Location</div><div class="info-value">Cedar Ridge Elementary School</div></div></li>
      <li class="info-item" style="height:56px"><span class="info-icon"><svg><use href="#i-search"/></svg></span><div><div class="info-label">Type</div><div class="info-value">Vacancy</div></div></li>
      <li class="info-item" style="height:60px"><span class="info-icon"><svg><use href="#i-people"/></svg></span><div><div class="info-label">Regular Staff</div><div class="info-value"><span class="ini">MH</span> Marco Hale</div></div></li>
      <li class="info-item" style="height:60px"><span class="info-icon"><svg><use href="#i-grid"/></svg></span><div><div class="info-label">Assignment Category</div><div class="info-value">Teacher</div></div></li>
      <li class="info-item" style="height:62px"><span class="info-icon"><svg><use href="#i-tree"/></svg></span><div><div class="info-label">Department</div><div class="info-value">-</div></div></li>
      <li class="info-item"><span class="info-icon"><svg><use href="#i-info"/></svg></span><div><div class="info-label">Description</div><div class="info-value">asdf<br>sffsd</div></div></li>
    </ul>
    <div class="panel" style="position:absolute;left:20px;top:627px;width:318px;height:160px;padding:12px 18px">
      <div class="panel-title" style="font-size:13px">Comments</div>
      <div style="display:flex;gap:20px;margin-top:10px">
        <div class="field" style="width:188px;height:56px;padding:6px 10px;font-size:11px;align-items:flex-start;color:var(--ink)">Write a comment or upload a file....</div>
        <div style="display:flex;flex-direction:column;gap:10px;padding-top:6px"><span class="pill teal">Post ➤</span><span class="pill purple">Upload ▮</span></div>
      </div>
      <div class="empty-note" style="margin-top:12px;padding:10px 0;font-size:12px">No comments or files uploaded</div>
    </div>
  </section>

  <!-- Assignments (compact) -->
  <section class="screen rounded" style="left:655px;top:100px;width:358px;height:775px;background:#f6f6f9">
    <div class="status"><span>9:45</span><svg><use href="#i-status"/></svg></div>
    <div class="brand" style="background:#fff"><div class="kebab"><i></i><i></i><i></i></div><div class="brand-name"><span class="brand-dot"></span>ShiftCover</div></div>
    <nav class="tabs" style="top:126px;gap:18px">
      <span class="tab active"><svg style="color:#fff"><use href="#i-clip"/></svg>My Assignments</span>
      <span class="tab"><svg style="color:var(--label)"><use href="#i-clock"/></svg>Available Openings</span>
      <span class="tab"><svg style="color:var(--label)"><use href="#i-clip"/></svg>My</span>
    </nav>
    <div class="assign-wrap list-sm" style="top:186px;height:600px">
      <div class="assign-head"><h2>My Assignments</h2><span class="help">?</span></div>
      <article class="assign-card"><div><div class="ac-label">Subbing For:</div><div class="ac-person"><span class="avatar photo" role="img" aria-label="Profile photo of Dana Ellis"></span><div><div class="ac-name">Dana Ellis</div><div class="ac-role">Teacher</div></div></div></div>
        <div class="ac-right"><span class="edit"><svg><use href="#i-edit"/></svg></span><div class="ac-meta">Location: <span class="v">CRES</span></div><div class="ac-meta">Status: <span class="badge complete">Complete</span></div><div class="ac-meta">Time Slots: <span class="t">09/02-09/02 (1h 0m).</span></div></div></article>
      <article class="assign-card"><div><div class="ac-label">Subbing For:</div><div class="ac-person"><span class="avatar">T</span><div><div class="ac-name">Extra duty</div><div class="ac-role">Teacher</div></div></div></div>
        <div class="ac-right"><span class="edit"><svg><use href="#i-edit"/></svg></span><div class="ac-meta">Location: <span class="v">CRES</span></div><div class="ac-meta">Status: <span class="badge complete">Complete</span></div><div class="ac-meta">Time Slots: <span class="t">07/1007/11 (1h 20m)</span></div></div></article>
      <article class="assign-card"><div><div class="ac-label">Subbing For:</div><div class="ac-person"><span class="avatar">MH</span><div><div class="ac-name">Marco Hale</div><div class="ac-role">Teacher</div></div></div></div>
        <div class="ac-right"><span class="edit"><svg><use href="#i-edit"/></svg></span><div class="ac-meta">Location: <span class="v">CRES</span></div><div class="ac-meta">Status: <span class="badge complete">Complete</span></div><div class="ac-meta">Time Slots: <span class="t">07/1007/11 (1h 20m)</span></div></div></article>
      <article class="assign-card"><div><div class="ac-label">Subbing For:</div><div class="ac-person"><span class="avatar photo" role="img" aria-label="Profile photo of Owen Price"></span><div><div class="ac-name">Owen Price</div><div class="ac-role">Administrator</div></div></div></div>
        <div class="ac-right"><span class="edit"><svg><use href="#i-edit"/></svg></span><div class="ac-meta">Location: <span class="v">CRES</span></div><div class="ac-meta">Status: <span class="badge active">Active</span></div><div class="ac-meta">Time Slots: <span class="t">07/26-08/07 (14h 15m)</span></div></div></article>
    </div>
  </section>

  <!-- Opening information (full working page) -->
  <section class="screen" style="left:1162px;top:94px;width:403px;height:1846px">
    <div class="status" style="top:18px"><span style="font-size:15px">9:45</span><svg><use href="#i-status"/></svg></div>
    <div class="brand"><div class="kebab"><i></i><i></i><i></i></div><div class="brand-name" style="margin-left:50px;font-size:38px"><span class="brand-dot"></span>ShiftCover</div></div>
    <h1 class="section-title" style="position:absolute;left:34px;top:136px;font-size:21px">Opening Information</h1>
    <div style="position:absolute;left:0;top:0;width:403px;height:1750px;overflow:hidden">
      <ul class="info-list" style="position:absolute;left:28px;top:192px">
        <li class="info-item" style="height:68px"><span class="info-icon" style="width:46px;height:46px"><svg><use href="#i-doc"/></svg></span><div><div class="info-label" style="font-size:18px">Summary</div><div class="info-value" style="font-size:17px">Testing-test</div></div></li>
        <li class="info-item" style="height:68px"><span class="info-icon" style="width:46px;height:46px"><svg><use href="#i-pin"/></svg></span><div><div class="info-label" style="font-size:18px">Location</div><div class="info-value" style="font-size:17px">Cedar Ridge Elementary School</div></div></li>
        <li class="info-item" style="height:61px"><span class="info-icon" style="width:46px;height:46px"><svg><use href="#i-search"/></svg></span><div><div class="info-label" style="font-size:18px">Type</div><div class="info-value" style="font-size:17px">Vacancy</div></div></li>
        <li class="info-item" style="height:67px"><span class="info-icon" style="width:46px;height:46px"><svg><use href="#i-people"/></svg></span><div><div class="info-label" style="font-size:18px">Regular Staff</div><div class="info-value" style="font-size:17px"><span class="ini">MH</span> Marco Hale</div></div></li>
        <li class="info-item" style="height:67px"><span class="info-icon" style="width:46px;height:46px"><svg><use href="#i-grid"/></svg></span><div><div class="info-label" style="font-size:18px">Assignment Category</div><div class="info-value" style="font-size:17px">Teacher</div></div></li>
        <li class="info-item" style="height:67px"><span class="info-icon" style="width:46px;height:46px"><svg><use href="#i-tree"/></svg></span><div><div class="info-label" style="font-size:18px">Department</div><div class="info-value" style="font-size:17px">-</div></div></li>
        <li class="info-item"><span class="info-icon" style="width:46px;height:46px"><svg><use href="#i-info"/></svg></span><div><div class="info-label" style="font-size:18px">Description</div><div class="info-value" style="font-size:17px">asdf<br>sffsd</div></div></li>
      </ul>

      <div class="panel" style="position:absolute;left:25px;top:696px;width:353px;height:178px;padding:14px 20px">
        <div class="panel-title" style="font-size:15px">Comments</div>
        <div style="display:flex;gap:24px;margin-top:10px">
          <div class="field" style="width:208px;height:62px;padding:8px 11px;align-items:flex-start;color:var(--ink)">Write a comment or upload a file....</div>
          <div style="display:flex;flex-direction:column;gap:10px;padding-top:6px"><span class="pill teal" style="font-size:11px;padding:2px 18px">Post ➤</span><span class="pill purple" style="font-size:11px;padding:2px 12px">Upload ▮</span></div>
        </div>
        <div class="empty-note" style="margin-top:12px;padding:11px 0;font-size:14px">No comments or files uploaded</div>
      </div>

      <div class="panel" style="position:absolute;left:25px;top:894px;width:353px;height:130px;padding:14px 20px">
        <div class="panel-title" style="font-size:15px">Additional Details</div>
        <div style="font-size:13px;color:var(--ink-soft);margin-top:10px">Parking Spot</div>
        <div class="field" style="height:40px;margin-top:12px"></div>
      </div>

      <div class="panel" style="position:absolute;left:25px;top:1043px;width:353px;height:182px;padding:14px 20px">
        <div class="panel-title" style="font-size:15px">Time Slots</div>
        <div style="display:flex;gap:6px;margin-top:14px"><span class="pill teal" style="font-size:11px">Accept ✔</span><span class="pill purple" style="font-size:11px">Withdraw ▮</span></div>
        <div class="field" style="height:40px;margin-top:8px;padding-left:10px;gap:10px;font-size:15px"><span style="width:20px;height:20px;border-radius:4px;background:#e3e3e8"></span>Date</div>
        <div class="field" style="height:40px;margin-top:8px;padding:0 14px 0 10px;gap:10px;font-size:15px"><span style="width:20px;height:20px;border-radius:4px;background:#e3e3e8"></span>3/19/2026<svg style="width:24px;height:24px;margin-left:auto"><use href="#i-cal"/></svg></div>
      </div>

      <div class="panel" style="position:absolute;left:25px;top:1240px;width:353px;height:182px;padding:14px 20px">
        <div class="panel-title" style="font-size:15px">From :</div>
        <div class="field" style="height:40px;margin-top:8px;padding:0 10px 0 14px;font-size:15px">9:30 AM<svg style="width:26px;height:26px;margin-left:auto;color:var(--label)"><use href="#i-clock"/></svg></div>
        <div class="panel-title" style="font-size:15px;margin-top:12px">To :</div>
        <div class="field" style="height:40px;margin-top:8px;padding:0 10px 0 14px;font-size:15px">12:30 PM<svg style="width:26px;height:26px;margin-left:auto;color:var(--label)"><use href="#i-clock"/></svg></div>
      </div>

      <div class="panel" style="position:absolute;left:25px;top:1442px;width:353px;height:154px;padding:18px 20px">
        <div style="font-size:13px;color:var(--ink-soft)"><span style="color:var(--label);font-weight:700">Current Assignment :</span> No Assignment</div>
        <div style="font-size:13px;color:var(--label);font-weight:700;margin-top:10px;display:flex;align-items:center;gap:12px">Status: <span class="badge active" style="font-size:11px;font-weight:400;padding:1px 20px">Active</span></div>
        <div class="field" style="height:40px;margin-top:26px;padding:0 14px 0 10px;gap:10px;font-size:15px"><span style="width:20px;height:20px;border-radius:4px;background:#e3e3e8"></span>3/19/2026<svg style="width:24px;height:24px;margin-left:auto"><use href="#i-cal"/></svg></div>
      </div>

      <div class="panel" style="position:absolute;left:25px;top:1612px;width:353px;height:182px;padding:14px 20px">
        <div class="panel-title" style="font-size:15px">From :</div>
        <div class="field" style="height:40px;margin-top:8px;padding:0 10px 0 14px;font-size:15px">2:30 AM<svg style="width:26px;height:26px;margin-left:auto;color:var(--label)"><use href="#i-clock"/></svg></div>
        <div class="panel-title" style="font-size:15px;margin-top:12px">To :</div>
        <div class="field" style="height:40px;margin-top:8px;padding:0 10px 0 14px;font-size:15px">4:00 PM<svg style="width:26px;height:26px;margin-left:auto;color:var(--label)"><use href="#i-clock"/></svg></div>
      </div>
    </div>
    <div style="position:absolute;right:26px;top:1764px;display:flex;gap:6px"><span class="pill teal" style="font-size:11px;padding:2px 16px">Save ✔</span><span class="pill purple" style="font-size:11px;padding:2px 14px">Close ✖</span></div>
    <span class="home-bar" style="bottom:18px"></span>
  </section>

  <!-- Side menu -->
  <section class="screen menu" style="left:107px;top:976px;width:403px;height:872px">
    <div class="brand" style="top:52px;justify-content:center"><div class="brand-name" style="font-size:38px"><span class="brand-dot"></span>ShiftCover</div></div>
    <ul class="nav">
      <li class="current"><svg><use href="#i-house"/></svg>Home</li>
      <li><svg style="color:#fff"><use href="#i-clock"/></svg>Available Openings</li>
      <li><svg style="color:#fff"><use href="#i-clip"/></svg>Assignments</li>
      <li><svg><use href="#i-hand"/></svg>Support</li>
    </ul>
    <div class="profile">
      <div class="profile-img" role="img" aria-label="Empty profile picture placeholder"></div>
      <div style="font-size:21px;margin:24px 0 18px">No Profile Image</div>
      <div class="btn-outline"><svg style="width:22px;height:22px"><use href="#i-tap"/></svg>Click Here</div>
      <div style="font-size:21px;margin-top:14px">Greta</div>
      <div style="font-size:21px;margin-top:6px">g.sub.2@example.com</div>
    </div>
    <div style="position:absolute;left:36px;right:36px;top:766px;height:1px;background:rgba(255,255,255,.25)"></div>
    <div class="btn-logout"><svg style="width:24px;height:24px"><use href="#i-exit"/></svg>Log Out</div>
  </section>

  <!-- Assignments (full) -->
  <section class="screen" style="left:634px;top:976px;width:403px;height:1169px;background:#f6f6f9">
    <div class="status" style="top:18px"><span style="font-size:15px">9:45</span><svg><use href="#i-status"/></svg></div>
    <div class="brand" style="background:#fff;top:48px;height:56px"><div class="kebab" style="margin-left:24px"><i></i><i></i><i></i></div><div class="brand-name" style="margin-left:48px;font-size:38px"><span class="brand-dot"></span>ShiftCover</div></div>
    <nav class="tabs" style="left:14px;top:138px;gap:18px">
      <span class="tab active" style="font-size:13px"><svg style="color:#fff"><use href="#i-clip"/></svg>My Assignments</span>
      <span class="tab" style="font-size:14px"><svg style="color:var(--label);width:20px;height:20px"><use href="#i-clock"/></svg>Available Openings</span>
      <span class="tab" style="font-size:14px"><svg style="color:var(--label);width:22px;height:20px"><use href="#i-clip"/></svg>My</span>
    </nav>
    <div style="position:absolute;left:14px;right:0;top:184px;height:1px;background:var(--line)"></div>
    <div class="assign-wrap list-lg" style="top:206px;height:918px;left:10px;right:10px">
      <div class="assign-head"><h2>My Assignments</h2><span class="help">?</span></div>
      <article class="assign-card"><div><div class="ac-label">Subbing For:</div><div class="ac-person"><span class="avatar photo" role="img" aria-label="Profile photo of Dana Ellis"></span><div><div class="ac-name">Dana Ellis</div><div class="ac-role">Teacher</div></div></div></div>
        <div class="ac-right"><span class="edit"><svg><use href="#i-edit"/></svg></span><div class="ac-meta">Location: <span class="v">CRES</span></div><div class="ac-meta">Status: <span class="badge complete">Complete</span></div><div class="ac-meta">Time Slots: <span class="t">09/02-09/02 (1h 0m).</span></div></div></article>
      <article class="assign-card"><div><div class="ac-label">Subbing For:</div><div class="ac-person"><span class="avatar">T</span><div><div class="ac-name">Extra duty</div><div class="ac-role">Teacher</div></div></div></div>
        <div class="ac-right"><span class="edit"><svg><use href="#i-edit"/></svg></span><div class="ac-meta">Location: <span class="v">CRES</span></div><div class="ac-meta">Status: <span class="badge complete">Complete</span></div><div class="ac-meta">Time Slots: <span class="t">07/1007/11 (1h 20m)</span></div></div></article>
      <article class="assign-card"><div><div class="ac-label">Subbing For:</div><div class="ac-person"><span class="avatar">MH</span><div><div class="ac-name">Marco Hale</div><div class="ac-role">Teacher</div></div></div></div>
        <div class="ac-right"><span class="edit"><svg><use href="#i-edit"/></svg></span><div class="ac-meta">Location: <span class="v">CRES</span></div><div class="ac-meta">Status: <span class="badge complete">Complete</span></div><div class="ac-meta">Time Slots: <span class="t">07/1007/11 (1h 20m)</span></div></div></article>
      <article class="assign-card"><div><div class="ac-label">Subbing For:</div><div class="ac-person"><span class="avatar photo" role="img" aria-label="Profile photo of Owen Price"></span><div><div class="ac-name">Owen Price</div><div class="ac-role">Administrator</div></div></div></div>
        <div class="ac-right"><span class="edit"><svg><use href="#i-edit"/></svg></span><div class="ac-meta">Location: <span class="v">CRES</span></div><div class="ac-meta">Status: <span class="badge active">Active</span></div><div class="ac-meta">Time Slots: <span class="t">07/26-08/07 (14h 15m)</span></div></div></article>
      <article class="assign-card"><div><div class="ac-label">Subbing For:</div><div class="ac-person"><span class="avatar photo" role="img" aria-label="Profile photo of Priya Lane"></span><div><div class="ac-name">Priya Lane</div><div class="ac-role">Teacher</div></div></div></div>
        <div class="ac-right"><span class="edit"><svg><use href="#i-edit"/></svg></span><div class="ac-meta">Location: <span class="v">CRES</span></div><div class="ac-meta">Status: <span class="badge canceled">Canceled</span></div><div class="ac-meta">Time Slots: <span class="t">07/31-07/31 (9h 0m)</span></div></div></article>
      <article class="assign-card"><div><div class="ac-label">Subbing For:</div><div class="ac-person"><span class="avatar photo" role="img" aria-label="Profile photo of Evan Brooks"></span><div><div class="ac-name">Evan Brooks</div><div class="ac-role">Teacher</div></div></div></div>
        <div class="ac-right"><span class="edit"><svg><use href="#i-edit"/></svg></span><div class="ac-meta">Location: <span class="v">CRES</span></div><div class="ac-meta">Status: <span class="badge active">Active</span></div><div class="ac-meta">Time Slots: <span class="t">08/04-08/04 (7h 0m)</span></div></div></article>
    </div>
    <span class="home-bar"></span>
  </section>

</main>
</body>
</html>
```